Buch-/E-Book-Cover
Zielgruppe
Unternehmensberater, Spezialbereiche Sales und Recruiting
Arbeiten mit der Wegweiser Methode
Zielgruppe sind Führungskräfte in der HR- oder Sales-Abteilung
Management consultant, specialising in sales and recruiting
Working with the Wayfinder Method
Target group are managers in the HR or sales department
Aufgabenstellung
Bitte keine Magneten, Zielscheiben, Schiffe etc. Das kommt so oft vor. Es geht um Touchpoints, die aufeinander abgestimmt sind. Wertigkeit, kreative und besondere Dinge.
Buchtitel (NEU!!!!!)
(Autorin) Heike Brandauer
(Subtitel aber darüber) Kunden Kompass Methode (KKM®)
(Haupttitel) Mit Freude, Leichtigkeit und Kreativität zu Ihrem Wunschkunden.
(Subtitel 2) Praxiserprobte Tipps für Ihren Vertriebserfolg (im Kreis)
– siehe Layout unten das wir für einen anderen Titel schon gemacht hatten –
Format: DIN A6, Taschenguide. Schnell zur Hand und schnell gelesen.
Please no magnets, targets, ships, etc. That happens so often. It's about touchpoints that are coordinated. Value, creative and special things.
Book title (NEW!!!!!)
(Author) Heike Brandauer
(Subtitle but above) Kunden Kompass Methode (KKM®)
(Main title) With Care, Flair and Curiosity to Every Perfect Client.
(Subtitle 2) Tested Ideas for Your Sales Growth (in a circle)
- see layout below which we had already done for another title -
Format: DIN A6, pocket guide. Quickly to hand and quickly read.

```html
<!DOCTYPE html>
<html lang="en">
<head>
<meta charset="utf-8">
<title>Book Cover – With Care, Flair and Curiosity</title>
<link rel="stylesheet" href="https://fonts.googleapis.com/css2?family=Anton&family=Montserrat:wght@500;600;700;800&display=swap">
<style>
  :root {
    --page-bg: #ffffff;
    --navy-edge: #1b222d;
    --navy-core: #293d55;
    --orange: #f0a02c;
    --white: #ffffff;
    --badge-ink: #1f2c3f;
  }
  html, body {
    margin: 0;
    padding: 0;
    width: 1200px;
    height: 1200px;
    overflow: hidden;
    background: var(--page-bg);
  }
  .canvas {
    position: relative;
    width: 1200px;
    height: 1200px;
  }
  .cover {
    position: absolute;
    left: 217px;
    top: 60px;
    width: 772px;
    height: 1087px;
    background: radial-gradient(ellipse 70% 55% at 45% 42%, var(--navy-core) 0%, #22303f 60%, var(--navy-edge) 100%);
    font-family: "Montserrat", sans-serif;
    overflow: hidden;
  }
  .series-title {
    position: absolute;
    top: 35px;
    left: 0;
    width: 100%;
    text-align: center;
    margin: 0;
    color: var(--white);
    font-weight: 600;
    font-size: 25px;
    letter-spacing: 2px;
  }
  .series-title sup { font-size: 10px; letter-spacing: 0; }
  .headline {
    position: absolute;
    left: 40px;
    top: 150px;
    width: 690px;
    height: 193px;
  }
  .headline text {
    font-family: "Anton", sans-serif;
    fill: var(--orange);
  }
  .main-title {
    position: absolute;
    left: 41px;
    top: 399px;
    margin: 0;
    color: var(--white);
    font-weight: 700;
    font-size: 62px;
    line-height: 91px;
    letter-spacing: 1px;
    text-transform: uppercase;
  }
  .main-title .accent { color: var(--orange); }
  .seal {
    position: absolute;
    left: 456px;
    top: 413px;
    width: 282px;
    height: 282px;
  }
  .seal text {
    font-family: "Montserrat", sans-serif;
    font-weight: 800;
    fill: var(--badge-ink);
  }
  .author {
    position: absolute;
    left: 0;
    bottom: 26px;
    width: 100%;
    text-align: center;
    margin: 0;
    color: var(--orange);
    font-weight: 600;
    font-size: 58px;
    letter-spacing: 1px;
  }
</style>
</head>
<body>
<div class="canvas">
  <article class="cover">
    <p class="series-title">Kunden Kompass Methode (KKM<sup>®</sup>)</p>

    <svg class="headline" viewBox="0 0 690 193" aria-label="NEW!!!!!">
      <text x="0" y="193" font-size="263" textLength="690" lengthAdjust="spacingAndGlyphs">NEW!!!!!</text>
    </svg>

    <h1 class="main-title">
      <span class="accent">With</span> Care,<br>
      Flair <span class="accent">and</span><br>
      Curiosity<br>
      <span class="accent">to</span> Every<br>
      Perfect Client
    </h1>

    <svg class="seal" viewBox="0 0 280 280" aria-label="Tested ideas for your sales growth">
      <defs>
        <linearGradient id="seal-rim" x1="0" y1="0" x2="1" y2="1">
          <stop offset="0" stop-color="#f6d57a"/>
          <stop offset="0.35" stop-color="#d9a53a"/>
          <stop offset="0.7" stop-color="#b37418"/>
          <stop offset="1" stop-color="#8a520c"/>
        </linearGradient>
        <linearGradient id="seal-ring" x1="0" y1="0" x2="1" y2="1">
          <stop offset="0" stop-color="#8a560f"/>
          <stop offset="0.5" stop-color="#c7902f"/>
          <stop offset="1" stop-color="#fbe9a6"/>
        </linearGradient>
        <linearGradient id="seal-face" x1="0" y1="0" x2="1" y2="0.4">
          <stop offset="0" stop-color="#d6ad55"/>
          <stop offset="0.5" stop-color="#f5df92"/>
          <stop offset="1" stop-color="#d4a94e"/>
        </linearGradient>
      </defs>
      <circle cx="140" cy="140" r="140" fill="url(#seal-rim)"/>
      <circle cx="140" cy="140" r="120" fill="url(#seal-ring)"/>
      <circle cx="140" cy="140" r="114" fill="url(#seal-face)"/>
      <g transform="rotate(9 140 140)">
        <text x="140" y="110" font-size="24" text-anchor="middle" letter-spacing="1">TESTED IDEAS</text>
        <text x="136" y="140" font-size="19" text-anchor="middle" letter-spacing="1">FOR YOUR SALES</text>
        <text x="136" y="182" font-size="42" text-anchor="middle" letter-spacing="1">GROWTH</text>
      </g>
    </svg>

    <p class="author">Heike Brandauer</p>
  </article>
</div>
</body>
</html>
```